Redesign www.brightlobco.com

I want a website designer to design my website for me. There is a site up right now but it's not complete because my clients can not pay for my services online. Whoever signs up for this project will have to work on a speedy schedule to be able to complete the new site within a week. I have all of the information online so now at www.brightlobco.com I can send you other files as well. Please let me know if you will be able to do this.

The site needs to be optimize for all platforms like, desktop, laptop, and smartphone.

I do have a quikfund account that we can link to the site to accept transactions.

Thank you,

Rolf

Target Market(s)

Tennis players

Coding

Coded - Design and coding required

Number of Pages Required

5+ page

Font styles to use
Sans Serif
Script

Colors
00a990
a4ce38
ffffff
fbee3f

Requirements
Must have
• Ability to read through the site and ensure that the functionality works. Must have some testing and QA background in order to perform thorough testing and quality assurance prior to delivery. I will prefer a WordPress template for the site.
Nice to have
• Not sure if I will need my own merchant account, but if that's the case, I can get one.

```html
<!DOCTYPE html>
<html lang="en">
<head>
<meta charset="utf-8">
<title>Brightlob Tennis &amp; Racket Services</title>
<link rel="stylesheet" href="https://fonts.googleapis.com/css2?family=Raleway:wght@300;400;500;600&display=swap">
<style>
  :root {
    --green: #a4ce38;
    --green-deep: #7fae1c;
    --teal: #00a990;
    --yellow: #fbee3f;
    --white: #ffffff;
    --ink: #4a4a4a;
    --ink-soft: #6b6b6b;
    --sky-top: #2f6fbf;
    --sky-mid: #5a8fd0;
    --sky-light: #b9cde6;
  }
  * { box-sizing: border-box; margin: 0; padding: 0; }
  html, body { width: 1200px; height: 1066px; overflow: hidden; background: var(--white); }
  body { font-family: "Raleway", sans-serif; color: var(--ink); }

  .site-header { position: relative; height: 69px; background: var(--white); }
  .brand {
    position: absolute; left: 241px; top: 20px;
    display: flex; align-items: center; gap: 8px;
    font-size: 20px; font-weight: 600; color: var(--green-deep); letter-spacing: 0.5px;
  }
  .brand-dot { width: 14px; height: 14px; border-radius: 50%; background: var(--green); }
  .utility-nav {
    position: absolute; right: 244px; top: 7px;
    display: flex; gap: 18px; font-size: 8px; color: var(--ink-soft); text-transform: uppercase;
  }
  .utility-nav span { display: flex; align-items: center; gap: 4px; }
  .utility-nav svg { width: 8px; height: 8px; }
  .menu-toggle {
    position: absolute; right: 244px; top: 39px;
    display: flex; align-items: center; gap: 6px; font-size: 13px; color: var(--ink);
  }

  .hero {
    position: relative; height: 416px;
    border-bottom: 2px solid var(--green);
  }
  .hero-photo {
    position: absolute; inset: 0;
    background:
      radial-gradient(ellipse at 70% 30%, var(--sky-light) 0%, transparent 45%),
      radial-gradient(ellipse at 25% 55%, rgba(255,255,255,0.55) 0%, transparent 40%),
      linear-gradient(160deg, var(--sky-mid) 0%, var(--sky-top) 55%, #2a62b0 100%);
  }
  .hero-copy { position: absolute; left: 239px; top: 108px; color: var(--white); }
  .hero-title {
    font-weight: 300; font-size: 44px; line-height: 1.05; letter-spacing: 0.5px;
    text-transform: uppercase;
  }
  .hero-title .line-two { font-size: 35px; display: block; margin-top: 4px; }
  .hero-rule { width: 326px; height: 1px; background: rgba(255,255,255,0.85); margin: 10px 0 12px; }
  .hero-sub { font-size: 14px; font-weight: 400; text-transform: uppercase; margin-left: 4px; }
  .btn-solid {
    display: inline-block; margin: 20px 0 0 4px; padding: 8px 22px;
    background: var(--yellow); color: var(--ink); font-size: 10px; text-transform: uppercase;
  }
  .slider-arrow { position: absolute; top: 198px; width: 12px; height: 18px; }
  .slider-arrow.prev { left: 12px; }
  .slider-arrow.next { right: 12px; }

  .welcome { text-align: center; padding-top: 34px; }
  .welcome-title { font-size: 20px; font-weight: 400; color: var(--green-deep); text-transform: uppercase; }
  .welcome-lead { font-size: 13px; color: var(--ink); margin-top: 8px; }
  .divider { display: flex; align-items: center; justify-content: center; margin: 14px auto 24px; width: 360px; }
  .divider i { flex: 1; height: 1px; background: var(--green); }
  .divider b { width: 9px; height: 9px; border: 1px solid var(--green); border-radius: 50%; margin: 0 3px; }
  .welcome-text { width: 560px; margin: 0 auto; font-size: 10px; line-height: 17px; color: var(--ink-soft); }
  .btn-outline {
    display: inline-block; margin-top: 22px; padding: 7px 22px;
    border: 1px solid var(--yellow); color: var(--yellow); font-size: 10px; text-transform: uppercase;
  }
</style>
</head>
<body>
  <header class="site-header">
    <div class="brand"><span class="brand-dot"></span>Brightlob</div>
    <nav class="utility-nav">
      <span><svg viewBox="0 0 10 10"><path d="M5 0a3.5 3.5 0 0 0-3.5 3.5C1.5 6 5 10 5 10s3.5-4 3.5-6.5A3.5 3.5 0 0 0 5 0z" fill="var(--green)"/></svg>Locations</span>
      <span><svg viewBox="0 0 10 10"><path d="M2 0l2 2.5-1 1.2a6 6 0 0 0 3.3 3.3l1.2-1L10 8 8.5 10C4 9.5.5 6 0 1.5z" fill="var(--green)"/></svg>555-014-2290</span>
      <span><svg viewBox="0 0 10 10"><rect x="1.5" y="0.5" width="7" height="9" fill="none" stroke="var(--green)"/><path d="M3 3h4M3 5h4M3 7h3" stroke="var(--green)"/></svg>Book Lessons</span>
    </nav>
    <div class="menu-toggle">MENU
      <svg width="13" height="10" viewBox="0 0 13 10"><g fill="var(--green)"><rect x="0" y="0" width="2" height="2"/><rect x="3" y="0" width="10" height="2"/><rect x="0" y="4" width="2" height="2"/><rect x="3" y="4" width="10" height="2"/><rect x="0" y="8" width="2" height="2"/><rect x="3" y="8" width="10" height="2"/></g></svg>
    </div>
  </header>

  <section class="hero">
    <div class="hero-photo" role="img" aria-label="Photo of a tennis racket against a blue cloudy sky with tennis balls flying through the air"></div>
    <svg class="slider-arrow prev" viewBox="0 0 12 18"><path d="M9 2L3 9l6 7" fill="none" stroke="var(--white)" stroke-width="1.2"/></svg>
    <svg class="slider-arrow next" viewBox="0 0 12 18"><path d="M3 2l6 7-6 7" fill="none" stroke="var(--white)" stroke-width="1.2"/></svg>
    <div class="hero-copy">
      <h1 class="hero-title">The more you<span class="line-two">sweat in training</span></h1>
      <div class="hero-rule"></div>
      <p class="hero-sub">The less you lose in matches</p>
      <a class="btn-solid">Learn more</a>
    </div>
  </section>

  <section class="welcome">
    <h2 class="welcome-title">Welcome</h2>
    <p class="welcome-lead">Brightlob Tennis &amp; Racket Services</p>
    <div class="divider"><i></i><b></b><i></i></div>
    <p class="welcome-text">Brightlob Tennis &amp; Racket Services activities (Lessons, Clinics, Team Practices, Video Analysis, Tournaments, etc) are run under the direction and leadership of Master Tennis Coach - Rolf Hartwell. Rolf is a well-known in tennis around the Northern Virginia Area. He has vast experience at teaching all levels of tennis, from the quick starter to touring professionals.</p>
    <a class="btn-outline">Learn more</a>
  </section>
</body>
</html>
```